Water Bottle Design

We are launching a water bottle and need a impactful design.

Target Market(s)

health conscious hipsters

Font styles to use
Sans Serif

Requirements
Must have
• Please include the logo (included) on one side of the bottle and these words on the other side of the bottle. "It’s simple, REUSE this bottle every day. Your action, will REDUCE the amount of waste produced. SAVE your body from drinking the harmful contaminants in your water from Non-BPA plastics. HELP someone else because proceeds from your purchase will help homeless veterans.
• We’re just two dudes that like to drink water and help people. #KindFlow"
• Use a total of two colors
• UPDATE: You do not have to use the bottle on the logo.
Nice to have
• The bottle itself is 34 ounces and looks like a normal water bottle. I will include the image in the files. We would need to be able to change the colors easily.
Should not have
• Do not use more than two colors. Colors should not be important to the design at this point.

```html
<!DOCTYPE html>
<html lang="en">
<head>
<meta charset="utf-8">
<title>KindFlow Bottle Label</title>
<link rel="stylesheet" href="https://fonts.googleapis.com/css2?family=Raleway:wght@300&family=Source+Sans+3:wght@400&family=Yellowtail&display=swap">
<style>
  :root {
    --ink: #2a2a2a;
    --brand-blue: #1f8fd6;
    --sky-light: #f4fafe;
    --sky-mid: #d6ecfa;
    --water-light: #bfe3f8;
    --water-mid: #5bb8ec;
    --water-deep: #1d8fd8;
    --panel: #ffffff;
    --panel-line: #c9d3da;
  }
  html, body {
    margin: 0;
    padding: 0;
    overflow: hidden;
    background: #ffffff;
  }
  .label {
    position: relative;
    width: 1200px;
    height: 368px;
    overflow: hidden;
    background: linear-gradient(90deg, var(--sky-mid) 0%, var(--sky-light) 35%, #ffffff 60%, var(--sky-light) 100%);
    font-family: "Source Sans 3", sans-serif;
    color: var(--ink);
  }
  .water-art {
    position: absolute;
    left: 0;
    top: 0;
    width: 1200px;
    height: 368px;
  }
  .brand-mark {
    position: absolute;
    left: 223px;
    top: 5px;
    width: 162px;
    height: 162px;
    box-sizing: border-box;
    border: 4px solid var(--brand-blue);
    border-radius: 50%;
    background: #ffffff;
  }
  .brand-name {
    position: absolute;
    left: 168px;
    top: 196px;
    margin: 0;
    font-family: "Raleway", sans-serif;
    font-weight: 300;
    font-size: 54px;
    line-height: 1;
    letter-spacing: -1px;
    color: var(--ink);
  }
  .message {
    position: absolute;
    left: 694px;
    top: 28px;
    width: 352px;
    margin: 0;
    font-size: 14.6px;
    line-height: 19.4px;
    text-align: justify;
    color: var(--ink);
  }
  .hashtag {
    position: absolute;
    left: 868px;
    top: 160px;
    margin: 0;
    font-family: "Yellowtail", cursive;
    font-size: 36px;
    line-height: 1;
    color: var(--ink);
  }
  .price-panel {
    position: absolute;
    left: 701px;
    top: 246px;
    width: 351px;
    height: 87px;
    box-sizing: border-box;
    background: var(--panel);
    border: 1px solid var(--panel-line);
    border-radius: 20px;
  }
  .price-panel p {
    margin: 0;
    position: absolute;
    left: 22px;
    top: 26px;
    font-size: 10px;
    color: var(--ink);
  }
</style>
</head>
<body>
<main class="label">
  <svg class="water-art" role="img" aria-label="Blue water splash with flowing waves and bubbles across the label" viewBox="0 0 1200 368" xmlns="http://www.w3.org/2000/svg">
    <defs>
      <linearGradient id="wave-fill" x1="0" y1="0" x2="0" y2="1">
        <stop offset="0" stop-color="var(--water-light)"/>
        <stop offset="0.5" stop-color="var(--water-mid)"/>
        <stop offset="1" stop-color="var(--water-deep)"/>
      </linearGradient>
    </defs>
    <path d="M0 200 C 200 170, 420 300, 700 260 S 1050 180, 1200 220 L 1200 368 L 0 368 Z" fill="url(#wave-fill)" opacity="0.85"/>
  </svg>

  <div class="brand-mark"></div>
  <h1 class="brand-name">KindFlow</h1>

  <p class="message">It's simple, REUSE this bottle every day. Your action, will REDUCE the amount of waste produced. SAVE your body from drinking the harmful contaminants in your water from Non-BPA plastics. HELP someone else because proceeds from your purchase will help homeless veterans.</p>
  <p class="hashtag">#KindFlow</p>

  <section class="price-panel">
    <p>Prices &amp; Stuff ..................</p>
  </section>
</main>
</body>
</html>
```